Creative Business Card for my Sail Boat.. Tide & Time

Going to order PLASTIC business cards for my boat.. she is a sailing vessel catamaran named Tide & Time..

Target Market(s)

to impress other boaters with a unique designed plastic card

Contact Information for Business Card

S/V Tide & Time
Captain Tom Brennick
brennick@tom.example
Mobile/WhatsApp 1-555-318-7062
www.sailtideandtime.example

Requirements
Must have
• Cool colors. logo.. and info in Business Card Details.. Thanks! Utilize clear or cloudy plastic in design. Thanks

```html
<!DOCTYPE html>
<html lang="en">
<head>
<meta charset="utf-8">
<title>Tide &amp; Time – Business Card</title>
<link rel="stylesheet" href="https://fonts.googleapis.com/css2?family=Open+Sans:wght@400;700&family=Roboto+Condensed:wght@400&display=swap">
<style>
  :root {
    --page: #ffffff;
    --card-light: #ede9e8;
    --card-dark: #512611;
    --red: #c21f28;
    --brown: #512611;
    --ink: #58585a;
    --ink-strong: #4a4a4c;
    --divider: #b5aca4;
    --taupe: #b8ada3;
    --yellow: #f7c815;
    --white: #ffffff;
  }
  * { margin: 0; padding: 0; box-sizing: border-box; }
  html, body {
    width: 968px; height: 1200px; overflow: hidden;
    background: var(--page);
  }
  .sheet { position: relative; width: 968px; height: 1200px; }

  .card { position: absolute; left: 4px; width: 960px; }
  .card--front { top: 4px; height: 571px; background: var(--card-light); }
  .card--back { top: 624px; height: 572px; background: var(--card-dark); }

  .holder-name {
    position: absolute; left: 94px; top: 62px;
    font-family: "Open Sans", sans-serif; font-size: 38px; letter-spacing: 0.5px;
    color: var(--ink); white-space: nowrap;
  }
  .holder-name .title { color: var(--red); font-weight: 700; }
  .holder-name .first { color: var(--ink-strong); font-weight: 700; }
  .holder-name .last { font-weight: 400; }

  .icon-band {
    position: absolute; left: 0; top: 133px; width: 146px; height: 305px;
    background: var(--red);
  }
  .icon-badge {
    position: absolute; left: 72px; width: 48px; height: 48px; border-radius: 50%;
    background: var(--white);
    box-shadow: 0 4px 5px rgba(0,0,0,0.35);
    display: flex; align-items: center; justify-content: center;
  }
  .icon-badge svg { width: 28px; height: 28px; }

  .contact {
    position: absolute; left: 172px;
    font-family: "Roboto Condensed", sans-serif; font-size: 29px;
    color: var(--ink); white-space: nowrap; line-height: 1;
  }
  .contact--address { top: 158px; line-height: 36px; }
  .contact--url { letter-spacing: -0.4px; }
  .address-rule {
    position: absolute; left: 172px; top: 238px; width: 75px; height: 4px;
    background: var(--red);
  }
  .divider {
    position: absolute; left: 529px; top: 133px; width: 3px; height: 305px;
    background: var(--divider);
  }

  .brand {
    position: absolute; text-align: center;
    font-family: "Open Sans", sans-serif; font-weight: 700;
    font-size: 52px; line-height: 58px;
  }
  .card--front .brand { left: 591px; top: 170px; width: 300px; color: var(--brown); }
  .card--back .brand { left: 331px; top: 172px; width: 300px; color: var(--taupe); }

  .follow {
    position: absolute; width: 167px; height: 28px; border-radius: 6px;
    font-family: "Open Sans", sans-serif; font-size: 17px; letter-spacing: 0.5px;
    display: flex; align-items: center; justify-content: center;
  }
  .card--front .follow { left: 658px; top: 331px; background: var(--red); color: var(--white); }
  .card--back .follow { left: 399px; top: 331px; background: var(--yellow); color: var(--brown); }

  .social { position: absolute; display: flex; gap: 10px; }
  .card--front .social { left: 658px; top: 368px; }
  .card--back .social { left: 399px; top: 371px; }
  .social-box {
    width: 49px; height: 49px; border-radius: 8px; border: 2px solid;
  }
  .card--front .social-box { border-color: var(--brown); }
  .card--back .social-box { border-color: var(--taupe); }

  .back-url {
    position: absolute; left: 0; top: 480px; width: 100%; text-align: center;
    font-family: "Roboto Condensed", sans-serif; font-size: 32px; color: var(--white);
  }
</style>
</head>
<body>
<div class="sheet">

  <section class="card card--front">
    <h1 class="holder-name"><span class="title">CAPTAIN</span> <span class="first">TOM</span> <span class="last">BRENNICK</span></h1>

    <div class="icon-band">
      <div class="icon-badge" style="top:26px">
        <svg viewBox="0 0 24 24"><path fill="#512611" d="M12 2a7 7 0 0 0-7 7c0 5 7 13 7 13s7-8 7-13a7 7 0 0 0-7-7zm0 9.5A2.5 2.5 0 1 1 12 6.5a2.5 2.5 0 0 1 0 5z"/></svg>
      </div>
      <div class="icon-badge" style="top:116px">
        <svg viewBox="0 0 24 24"><path fill="#512611" d="M6.6 10.8a15 15 0 0 0 6.6 6.6l2.2-2.2a1 1 0 0 1 1-.25 11.4 11.4 0 0 0 3.6.57 1 1 0 0 1 1 1V20a1 1 0 0 1-1 1A17 17 0 0 1 3 4a1 1 0 0 1 1-1h3.5a1 1 0 0 1 1 1c0 1.25.2 2.45.57 3.57a1 1 0 0 1-.25 1z"/></svg>
      </div>
      <div class="icon-badge" style="top:171px">
        <svg viewBox="0 0 24 24"><rect x="2.5" y="5" width="19" height="14" fill="none" stroke="#512611" stroke-width="2"/><path d="M2.5 5l9.5 8 9.5-8M2.5 19l7-6.5M21.5 19l-7-6.5" fill="none" stroke="#512611" stroke-width="2"/></svg>
      </div>
      <div class="icon-badge" style="top:225px">
        <svg viewBox="0 0 24 24" fill="none" stroke="#512611" stroke-width="1.8"><circle cx="12" cy="12" r="9.5"/><ellipse cx="12" cy="12" rx="4" ry="9.5"/><path d="M2.5 12h19M4 7h16M4 17h16"/></svg>
      </div>
    </div>

    <p class="contact contact--address">123 Stree, Your City<br>Country 1234</p>
    <div class="address-rule"></div>
    <p class="contact" style="top:256px">1-555-318-7062</p>
    <p class="contact" style="top:311px">brennick@tom.example</p>
    <p class="contact contact--url" style="top:365px">www.sailtideandtime.example</p>

    <div class="divider"></div>

    <p class="brand">Tide &amp;<br>Time</p>
    <p class="follow">follow us on:</p>
    <div class="social">
      <span class="social-box" role="img" aria-label="Social network link"></span>
      <span class="social-box" role="img" aria-label="Social network link"></span>
      <span class="social-box" role="img" aria-label="Social network link"></span>
    </div>
  </section>

  <section class="card card--back">
    <p class="brand">Tide &amp;<br>Time</p>
    <p class="follow">follow us on:</p>
    <div class="social">
      <span class="social-box" role="img" aria-label="Social network link"></span>
      <span class="social-box" role="img" aria-label="Social network link"></span>
      <span class="social-box" role="img" aria-label="Social network link"></span>
    </div>
    <p class="back-url">www.sailtideandtime.example</p>
  </section>

</div>
</body>
</html>
```